Website for IT Security Company in Austria with small and medium business customer base

I own a one man IT security company with a customer small to medium business customer base and need a professional looking website that contains the following information:
- Home page: About the company....
- Services: The services that I offer. It would be nice to have icons if possible (e.g Quorel Ledger icon, digital certificate icon, ...) but this is not a must have.
- About me
- Blog: This is not a must have. It would be ok to just link it to an external blog.
- Impressum
- Contact: No form, just telephone number and e-mail address
- Anything else that you think is necessary for a professional appearance
Also I attached the company design. I do have all source files for the logo if required.

Target Market(s)

Small and medium business of all branches located in Austria

Industry/Entity Type

Cyber Security

Coding

Coded - Design and coding required

Number of Pages Required

5+ page

Font styles to use
Serif
Sans Serif
Other font styles liked:
• Bitsumishi, Bankgothic

Colors

Designer to choose only greyscale colors for use in the design.

Requirements
Must have
• The website must be a mobile-first design.
The design should not be too colorful or playful.
The logo should be used as much as possible
Navigation bar with multi drop-down menu for the services that I offer.
Example:
Services
-> Implementations
-> Implementation Service A
-> Implementation Service B
-> Security Audit
-> Audit A
-> Audit B
Maybe you could have service cards that describe the services briefly and on click redirect to the site that describes the service in detail.
End of example
Logo
contact
impressum
services that I offer
about me
about the company
Nice to have
• Icons would be nice (e.g. house for homepage, letter for contact, ...)
Also for the services I offer icons would be nice (Quorel Ledger, digtial certificates, hacking, security auditing)
For the fonts I have only sugested Bitsumishi and Bankgothic as they are part of my logo. No sure if you feel they make sense as part of the website
Should not have
• forms.
I want to the site to be made as easy as possible (HTML5, CSS, javascript/php/.net)
I do not want a wordpress template or suchlike.

```html
<!DOCTYPE html>
<html lang="en">
<head>
<meta charset="utf-8">
<title>Ferrolith Guard – IT Security</title>
<link href="https://fonts.googleapis.com/css2?family=Lato:wght@400;700;900&display=swap" rel="stylesheet">
<style>
:root{
  --ink:#111;
  --text:#333;
  --muted:#555;
  --blue:#1a73d9;
  --blue-dark:#0f5cb5;
  --soft:#f3f0f0;
  --soft2:#f4f2f3;
  --rule:#9a9a9a;
  --white:#fff;
  --black:#000;
}
*{box-sizing:border-box;margin:0;padding:0}
html,body{width:1200px;height:3102px;overflow:hidden}
body{font-family:'Lato',sans-serif;color:var(--text);background:var(--white);position:relative}
a{color:inherit;text-decoration:none}

/* header */
.site-header{position:absolute;left:0;top:0;width:1200px;height:126px;background:var(--white)}
.brand{position:absolute;left:131px;top:30px;display:flex;align-items:center;gap:10px}
.brand-mark{width:26px;height:26px;background:var(--ink)}
.brand-name{font-weight:900;font-size:25px;letter-spacing:1px;color:var(--ink);line-height:1}
.brand-sub{position:absolute;left:36px;top:32px;font-size:10px;letter-spacing:7px;color:var(--ink);font-weight:400}
.contact-bar{position:absolute;top:26px;right:131px;display:flex;gap:50px}
.contact-item{display:flex;align-items:center;gap:14px}
.contact-item svg{width:30px;height:30px}
.contact-label{font-size:12px;color:var(--ink);line-height:1.3}
.contact-value{font-size:15px;color:var(--ink)}
.contact-value.big{font-size:19px;font-weight:700}
.main-nav{position:absolute;top:89px;right:131px;display:flex;gap:34px;font-size:14px;color:var(--ink)}
.main-nav a{position:relative;padding-bottom:10px}
.main-nav a.active::after{content:"";position:absolute;left:0;right:0;bottom:0;height:2px;background:var(--ink)}

/* hero */
.hero{position:absolute;left:0;top:126px;width:1200px;height:578px}
.hero-photo{position:absolute;inset:0;background:linear-gradient(100deg,#8d99b3 0%,#4d6292 25%,#2c3f78 45%,#1e3f86 60%,#5b77ae 80%,#9fb3d6 100%)}
.hero-copy{position:absolute;left:130px;top:244px;color:var(--white)}
.hero-title{font-size:60px;font-weight:900;letter-spacing:1px;line-height:1}
.hero-sub{font-size:20px;margin-top:14px}
.btn-light{display:inline-block;margin-top:28px;margin-left:2px;background:var(--white);color:var(--ink);font-size:16px;padding:14px 19px}
.hero-dots{position:absolute;left:563px;top:535px;display:flex;gap:11px}
.hero-dots span{width:7px;height:7px;border-radius:50%;background:var(--white)}
.hero-dots span.on{background:#7cc242}

/* section headings */
.section-title{font-size:24px;font-weight:900;color:var(--ink);text-align:center;letter-spacing:.5px}
.title-rule{width:50px;height:2px;background:var(--rule);margin:18px auto 0}

/* services */
.services{position:absolute;left:0;top:704px;width:1200px;height:502px}
.services .section-title{margin-top:36px}
.service-card{position:absolute;top:113px;width:293px;height:335px;background:var(--white);box-shadow:0 3px 14px rgba(0,0,0,.08);text-align:center}
.service-card svg{margin-top:30px;width:74px;height:70px}
.service-name{margin-top:24px;font-size:14px;font-weight:700;color:var(--ink)}
.service-text{margin:22px auto 0;width:220px;font-size:13px;line-height:20px;color:var(--muted)}
.btn-outline{display:inline-block;margin-top:29px;border:2px solid var(--blue);color:var(--blue);font-size:11px;font-weight:700;padding:6px 11px}

/* welcome */
.welcome{position:absolute;left:0;top:1206px;width:1200px;height:481px;background:var(--soft)}
.welcome-photo{position:absolute;left:136px;top:57px;width:431px;height:373px;background:linear-gradient(135deg,#0c1a33,#16365d 55%,#2a5a8c)}
.welcome-copy{position:absolute;left:642px;top:50px;width:430px}
.welcome-kicker{font-size:18px;color:var(--ink)}
.welcome-title{font-size:33px;font-weight:900;color:var(--ink);margin-top:4px}
.rule-left{width:50px;height:2px;background:var(--rule);margin-top:16px}
.welcome-copy p{font-size:16px;line-height:24px;color:var(--text);margin-top:24px}
.btn-blue{display:inline-block;background:var(--blue);color:var(--white);font-size:12px;font-weight:700;padding:10px 13px}
.welcome-copy .btn-blue{margin-top:22px;margin-left:2px}

/* why */
.why{position:absolute;left:0;top:1687px;width:1200px;height:497px;background:var(--white);overflow:hidden}
.why-accent{position:absolute;inset:0;background:var(--blue);clip-path:polygon(589px 0,1200px 0,1200px 497px,614px 497px)}
.why-photo{position:absolute;inset:0;background:linear-gradient(160deg,#0e3c78,#2f7cc2 45%,#9ecff0 52%,#2b6db0 60%,#0a2f63);clip-path:polygon(590px 0,1200px 0,1200px 497px,626px 497px)}
.why-copy{position:absolute;left:155px;top:80px;width:360px;text-align:center}
.why-copy h2{font-size:24px;font-weight:900;color:var(--ink)}
.why-copy p{font-size:16px;line-height:24px;margin-top:26px;color:var(--text)}
.why-copy .btn-blue{margin-top:33px;font-size:13px;padding:11px 14px}

/* blog */
.blog{position:absolute;left:0;top:2184px;width:1200px;height:573px;background:var(--soft2)}
.blog .section-title{margin-top:46px}
.blog-card{position:absolute;top:133px;width:297px;height:388px;background:var(--white);box-shadow:0 3px 14px rgba(0,0,0,.06)}
.blog-photo{height:189px}
.blog-body{padding:24px 24px 0}
.blog-title{font-size:13px;font-weight:900;color:var(--ink);line-height:20px;text-transform:uppercase}
.blog-text{font-size:12px;line-height:18px;color:var(--muted);margin-top:12px}
.blog-body .btn-blue{margin-top:16px;font-size:11px;font-weight:400;padding:8px 11px}

/* footer */
.site-footer{position:absolute;left:0;top:2757px;width:1200px;height:345px;background:var(--black);color:var(--white)}
.footer-brand{position:absolute;left:133px;top:96px;width:288px;text-align:center}
.footer-brand .mark{width:44px;height:44px;background:var(--white);margin:0 auto 14px}
.footer-brand .name{font-size:27px;font-weight:900;letter-spacing:1px}
.footer-brand .sub{font-size:10px;letter-spacing:9px;margin-top:6px}
.footer-col{position:absolute;top:50px}
.footer-col h3{font-size:13px;font-weight:900;letter-spacing:.5px}
.footer-menu{list-style:none;margin-top:23px;font-size:11px;line-height:20px}
.footer-list{list-style:none;margin-top:20px}
.footer-list li{display:flex;align-items:flex-start;gap:12px;font-size:11px;line-height:16px;margin-bottom:18px}
.footer-list .ic{flex:none;width:24px;height:24px;border-radius:50%;background:var(--white);display:flex;align-items:center;justify-content:center;margin-top:2px}
.footer-list .ic svg{width:12px;height:12px}
.footer-rule{position:absolute;left:110px;right:157px;top:266px;height:1px;background:#333}
.copyright{position:absolute;left:489px;top:309px;font-size:9px;color:#ccc}
</style>
</head>
<body>

<header class="site-header">
  <a class="brand" href="#">
    <span class="brand-mark"></span>
    <span class="brand-name">FERROLITH GUARD</span>
    <span class="brand-sub">IT SECURITY</span>
  </a>
  <div class="contact-bar">
    <div class="contact-item">
      <svg viewBox="0 0 30 30" fill="none" stroke="#111" stroke-width="1.6"><rect x="3" y="7" width="24" height="17"/><path d="M3 7l12 10 12-10"/></svg>
      <div><div class="contact-label">E MAIL US</div><div class="contact-value">office@ferrolithguard.at</div></div>
    </div>
    <div class="contact-item">
      <svg viewBox="0 0 30 30" fill="none" stroke="#111" stroke-width="1.6"><path d="M7 4l5 5-3 3c2 4 5 7 9 9l3-3 5 5-4 4C13 26 4 17 3 8z"/><path d="M17 6a8 8 0 0 1 7 7M17 2a12 12 0 0 1 11 11"/></svg>
      <div><div class="contact-label">CALL US</div><div class="contact-value big">+43 660 41200378</div></div>
    </div>
  </div>
  <nav class="main-nav">
    <a class="active" href="#">HOME</a>
    <a href="#">SERVICES</a>
    <a href="#">ABOUT ME</a>
    <a href="#">BLOG</a>
    <a href="#">IMPRESSUM</a>
    <a href="#">CONTACT</a>
  </nav>
</header>

<section class="hero">
  <div class="hero-photo" role="img" aria-label="Businessman touching a glowing digital security shield with a keyhole over blue data"></div>
  <div class="hero-copy">
    <h1 class="hero-title">IT SECURITY</h1>
    <p class="hero-sub">Increasing IT security could be quite easy</p>
    <a class="btn-light" href="#">READ MORE</a>
  </div>
  <div class="hero-dots"><span></span><span></span><span class="on"></span><span></span><span></span></div>
</section>

<section class="services">
  <h2 class="section-title">OUR SERVICES</h2>
  <div class="title-rule"></div>

  <article class="service-card" style="left:131px">
    <svg viewBox="0 0 74 70" fill="none" stroke="#1a73d9" stroke-width="2"><rect x="4" y="5" width="66" height="60" rx="3"/><rect x="10" y="11" width="54" height="48"/><circle cx="37" cy="35" r="8"/><circle cx="37" cy="35" r="14" stroke-dasharray="5 4"/></svg>
    <h3 class="service-name">IMPLEMETATION</h3>
    <p class="service-text">Lorem ipsum dolor sit amet, cons ectetur adipiscing elit, sed do eius mod tempor incididunt ut labore et dolore magna aliqua</p>
    <a class="btn-outline" href="#">READ MORE</a>
  </article>

  <article class="service-card" style="left:453px">
    <svg viewBox="0 0 74 70" fill="none" stroke="#1a73d9" stroke-width="2"><path d="M6 6h62v42H30l-12 12V48H6z"/><path d="M18 22l2 4 4 1-3 3 1 4-4-2-4 2 1-4-3-3 4-1zM37 22l2 4 4 1-3 3 1 4-4-2-4 2 1-4-3-3 4-1zM56 22l2 4 4 1-3 3 1 4-4-2-4 2 1-4-3-3 4-1z"/><path d="M16 41h30"/></svg>
    <h3 class="service-name">SECURITY REVIEW</h3>
    <p class="service-text">Lorem ipsum dolor sit amet, cons ectetur adipiscing elit, sed do eius mod tempor incididunt ut labore et dolore magna aliqua</p>
    <a class="btn-outline" href="#">READ MORE</a>
  </article>

  <article class="service-card" style="left:775px">
    <svg viewBox="0 0 74 70" fill="none" stroke="#1a73d9" stroke-width="5" stroke-linejoin="round"><path d="M37 5c8 6 16 8 25 8 0 26-8 40-25 50C20 53 12 39 12 13c9 0 17-2 25-8z"/><path d="M26 34l9 9 28-28" stroke-linecap="round"/></svg>
    <h3 class="service-name">SECURITY OPTIMIZATION</h3>
    <p class="service-text">Lorem ipsum dolor sit amet, cons ectetur adipiscing elit, sed do eius mod tempor incididunt ut labore et dolore magna aliqua</p>
    <a class="btn-outline" href="#">READ MORE</a>
  </article>
</section>

<section class="welcome">
  <div class="welcome-photo" role="img" aria-label="IT administrator with a laptop in a server room"></div>
  <div class="welcome-copy">
    <div class="welcome-kicker">WELCOME TO</div>
    <h2 class="welcome-title">FERROLITH GUARD</h2>
    <div class="rule-left"></div>
    <p>In my almost 20 years of experience as an IT administrator, trainer, consultant and solution architect, I have been able to work for many companies in different industries and sizes.</p>
    <p>IT security, especially in the Veloria environment, has emerged as my greatest passion. Since then I have been supporting companies in realizing their security requirements.</p>
    <a class="btn-blue" href="#">READ MORE</a>
  </div>
</section>

<section class="why">
  <div class="why-accent"></div>
  <div class="why-photo" role="img" aria-label="Two hands shaking amid streams of blue digital data"></div>
  <div class="why-copy">
    <h2>WHY FERROLITH GUARD?</h2>
    <div class="title-rule"></div>
    <p>In the best case scenario, IT security should cost as few of your valuable resources as possible. With my help, you do not have to lift a heavy oak shield in the figurative sense, but only use an incomparably lighter but equally hard one made of carbon. So you can continue to put your strength into your work.</p>
    <a class="btn-blue" href="#">READ MORE</a>
  </div>
</section>

<section class="blog">
  <h2 class="section-title">LATEST BLOG</h2>
  <div class="title-rule"></div>

  <article class="blog-card" style="left:131px">
    <div class="blog-photo" role="img" aria-label="Hand holding a tablet projecting a glowing globe" style="background:linear-gradient(135deg,#0b1e2e,#1d4f74 50%,#0b1e2e)"></div>
    <div class="blog-body">
      <h3 class="blog-title">Lorem ipsum dolor sit amet conse ctetur adipiscing elit.</h3>
      <p class="blog-text">Sed ut perspiciatis unde omnis iste natus error sit voluptatem accusantium dolore mque laudantium, totam.</p>
      <a class="btn-blue" href="#">READ MORE</a>
    </div>
  </article>

  <article class="blog-card" style="left:452px">
    <div class="blog-photo" role="img" aria-label="Businessman's hands protecting a data privacy padlock symbol" style="background:linear-gradient(135deg,#0d1a2a,#233d5c 55%,#0d1a2a)"></div>
    <div class="blog-body">
      <h3 class="blog-title">But I must explain to you how all this mistaken idea</h3>
      <p class="blog-text">Nor again is there anyone who loves or pursues or desires to obtain pain of itself, because it is pain, but because.</p>
      <a class="btn-blue" href="#">READ MORE</a>
    </div>
  </article>

  <article class="blog-card" style="left:771px">
    <div class="blog-photo" role="img" aria-label="Laptop with translucent security interface overlays" style="background:linear-gradient(135deg,#e4edf5,#a9c1d8 55%,#dfe8f1)"></div>
    <div class="blog-body">
      <h3 class="blog-title">Sed quia non numquam eius modi tempora</h3>
      <p class="blog-text">Nor again is there anyone who loves or pursues or desires to obtain pain of itself, because it is pain, but because.</p>
      <a class="btn-blue" href="#">READ MORE</a>
    </div>
  </article>
</section>

<footer class="site-footer">
  <div class="footer-brand">
    <div class="mark"></div>
    <div class="name">FERROLITH GUARD</div>
    <div class="sub">IT SECURITY</div>
  </div>

  <div class="footer-col" style="left:488px">
    <h3>MENU</h3>
    <ul class="footer-menu">
      <li>HOME</li><li>SERVICES</li><li>ABOUT ME</li><li>BLOG</li><li>IMPRESSUM</li><li>CONTACT</li>
    </ul>
  </div>

  <div class="footer-col" style="left:675px">
    <h3>CONTACT US</h3>
    <ul class="footer-list">
      <li><span class="ic"><svg viewBox="0 0 12 12"><path d="M6 1a3.5 3.5 0 0 0-3.5 3.5C2.5 7 6 11 6 11s3.5-4 3.5-6.5A3.5 3.5 0 0 0 6 1z" fill="#000"/><circle cx="6" cy="4.5" r="1.2" fill="#fff"/></svg></span><span>2750 Marlow Street<br>Linden, OR 97120</span></li>
      <li><span class="ic"><svg viewBox="0 0 12 12"><path d="M3 1l2 2-1 1.5c.8 1.5 2 2.7 3.5 3.5L9 7l2 2-1.5 1.5C5 10 2 7 1.5 2.5z" fill="#000"/></svg></span><span>Call Us<br>+43 660 41200378</span></li>
      <li><span class="ic"><svg viewBox="0 0 12 12"><rect x="1.5" y="3" width="9" height="6.5" fill="#000"/><path d="M1.5 3l4.5 3.5L10.5 3" stroke="#fff" fill="none"/></svg></span><span>E mail Us<br>office@ferrolithguard.at</span></li>
    </ul>
  </div>

  <div class="footer-col" style="left:938px">
    <h3>FOLLOW US</h3>
    <ul class="footer-list">
      <li><span class="ic"></span><span>Like us on<br>CHATTERFEED</span></li>
      <li><span class="ic"></span><span>Follow us on<br>CHIRPLINE</span></li>
      <li><span class="ic"></span><span>Follow us on<br>WORKRING</span></li>
    </ul>
  </div>

  <div class="footer-rule"></div>
  <p class="copyright">Copyright © 2021 All Rights Reserved</p>
</footer>

</body>
</html>
```